A business selling natural soaps online and in farmers markets. I want it to reflect local commerce and natural lifestyle. My colors are olive green and saddle brown. I want the dimensions to be 2.25 x 3.25" with matte finish.
Updates

The name of my company is Fern Hollow Soapworks, LLC

Industry/Entity Type

Business

```html
<!DOCTYPE html>
<html lang="en">
<head>
<meta charset="utf-8">
<title>Fern Hollow Soapworks, LLC – Business Card</title>
<link rel="stylesheet" href="https://fonts.googleapis.com/css2?family=Source+Sans+3:wght@400&family=Arimo:wght@400&family=Tinos:wght@700&display=swap">
<style>
  :root {
    --card-green: #a6c47c;
    --stroke-green: #8db556;
    --stroke-deep: #7aa843;
    --mark-tan: #c9bca3;
    --ink: #111111;
    --paper: #ffffff;
  }
  html, body {
    margin: 0;
    padding: 0;
    width: 1200px;
    height: 839px;
    overflow: hidden;
    background: var(--card-green);
  }
  .card {
    position: relative;
    width: 1200px;
    height: 839px;
    overflow: hidden;
    background: var(--card-green);
  }
  .card__texture {
    position: absolute;
    inset: 0;
    display: block;
  }
  .brand-mark {
    position: absolute;
    left: 47px;
    top: 96px;
    width: 340px;
    height: 447px;
    background: var(--mark-tan);
  }
  .website {
    position: absolute;
    left: 391px;
    top: 197px;
    margin: 0;
    font-family: "Source Sans 3", "Myriad Pro", sans-serif;
    font-weight: 400;
    font-size: 88px;
    line-height: 1;
    white-space: nowrap;
    color: var(--ink);
  }
  .owner {
    position: absolute;
    left: 520px;
    top: 324px;
    width: 520px;
    margin: 0;
    text-align: center;
    font-family: "Arimo", Arial, sans-serif;
    font-size: 55px;
    line-height: 81px;
    color: var(--ink);
  }
  .email {
    position: absolute;
    left: 430px;
    top: 609px;
    width: 700px;
    margin: 0;
    text-align: center;
    font-family: "Tinos", "Times New Roman", serif;
    font-weight: 700;
    font-size: 50px;
    line-height: 1;
    white-space: nowrap;
    color: var(--ink);
  }
  .rule {
    position: absolute;
    left: 61px;
    top: 672px;
    width: 1086px;
    height: 5px;
    background: var(--ink);
  }
  .company {
    position: absolute;
    left: 48px;
    top: 676px;
    margin: 0;
    font-family: "Source Sans 3", "Myriad Pro", sans-serif;
    font-weight: 400;
    font-size: 93px;
    line-height: 1;
    white-space: nowrap;
    color: var(--paper);
  }
</style>
</head>
<body>
  <main class="card">
    <svg class="card__texture" width="1200" height="839" viewBox="0 0 1200 839" role="img" aria-label="Textured green brush strokes painted vertically across the card background">
      <defs>
        <linearGradient id="strokeWash" x1="0" y1="0" x2="1" y2="0">
          <stop offset="0" stop-color="#a6c47c"/>
          <stop offset="0.06" stop-color="#8db556"/>
          <stop offset="0.14" stop-color="#7aa843"/>
          <stop offset="0.24" stop-color="#93b95d"/>
          <stop offset="0.34" stop-color="#8db556"/>
          <stop offset="0.44" stop-color="#9dc06c"/>
          <stop offset="0.54" stop-color="#89b351"/>
          <stop offset="0.64" stop-color="#98bc63"/>
          <stop offset="0.76" stop-color="#8db556"/>
          <stop offset="0.88" stop-color="#96bb60"/>
          <stop offset="0.95" stop-color="#8db556"/>
          <stop offset="1" stop-color="#a6c47c"/>
        </linearGradient>
        <linearGradient id="edgeFade" x1="0" y1="0" x2="0" y2="1">
          <stop offset="0" stop-color="#a6c47c" stop-opacity="0.9"/>
          <stop offset="0.12" stop-color="#a6c47c" stop-opacity="0"/>
          <stop offset="0.85" stop-color="#a6c47c" stop-opacity="0"/>
          <stop offset="1" stop-color="#a6c47c" stop-opacity="0.8"/>
        </linearGradient>
      </defs>
      <rect x="0" y="0" width="1200" height="839" fill="url(#strokeWash)"/>
      <rect x="0" y="0" width="1200" height="839" fill="url(#edgeFade)"/>
    </svg>

    <div class="brand-mark" role="img" aria-label="Fern Hollow Soapworks brand mark"></div>

    <p class="website">fernhollowsoap.com</p>

    <p class="owner">Carla Bennett,<br>Owner</p>

    <p class="email">info@fernhollowsoap.com</p>

    <div class="rule"></div>

    <h1 class="company">Fern Hollow Soapworks, LLC</h1>
  </main>
</body>
</html>
```